July 4th Campaign Banners with landing page

6 sizes of banners with same messaging. Layered photoshop files (psd) must be included.

Refer to VelmarSound.com for style reference (and attached style guide)

Banner sizes:
Affiliate banners - 300x250, 728x90, 160x600
Website header - 1180x300, sidebar - 280x285,
email header - 600x500

Please follow palette in style guide but use san serif fonts only.

Target Market(s)

males 35-50 years old, high income, high education

Industry/Entity Type

Campaign

Font styles to use
Sans Serif

Requirements
Must have
• Call to action - "Shop Now"
Should not have
• Follow style guide

```html
<!DOCTYPE html>
<html lang="en">
<head>
<meta charset="utf-8">
<title>VelmarSound July 4th Banner Set</title>
<link rel="stylesheet" href="https://fonts.googleapis.com/css2?family=Roboto+Condensed:wght@700&family=Open+Sans:wght@400&display=swap">
<style>
  :root {
    --board: #4a4a4a;
    --red-deep: #5e0508;
    --red-mid: #8c0f14;
    --red-light: #a3181d;
    --flag-blue: #3b3f86;
    --flag-red: #c8213a;
    --flag-white: #f4f2f4;
    --speaker-dark: #1c1c1e;
    --speaker-mid: #3a3a3d;
    --white: #ffffff;
    --brand-ink: #2a2a2a;
    --brand-mark: #a3181d;
  }
  * { box-sizing: border-box; margin: 0; padding: 0; }
  html, body { width: 1200px; height: 1084px; overflow: hidden; }
  body {
    background: linear-gradient(180deg, #555 0%, var(--board) 60%, #3e3e3e 100%);
    position: relative;
    font-family: "Roboto Condensed", "Arial Narrow", sans-serif;
  }
  .banner {
    position: absolute;
    overflow: hidden;
    background: radial-gradient(ellipse at 65% 55%, var(--red-light) 0%, var(--red-mid) 45%, var(--red-deep) 100%);
    box-shadow: 6px 8px 14px rgba(0,0,0,.45);
  }
  .flag { position: absolute; display: block; }
  .flag .union { fill: var(--flag-blue); }
  .speakers {
    position: absolute;
    background: linear-gradient(160deg, var(--speaker-mid) 0%, var(--speaker-dark) 70%);
    z-index: 2;
  }
  .footer {
    position: absolute; left: 0; right: 0; bottom: 0;
    background: var(--white);
    z-index: 1;
  }
  .brand {
    position: absolute;
    display: flex; align-items: center; gap: 5px;
    font-family: "Open Sans", sans-serif;
    font-weight: 400;
    color: var(--brand-ink);
    white-space: nowrap;
  }
  .brand::before {
    content: ""; display: block;
    width: .9em; height: .9em;
    background: var(--brand-mark);
  }
  .cta {
    position: absolute;
    z-index: 3;
    color: var(--white);
    font-weight: 700;
    line-height: .96;
    letter-spacing: .01em;
    text-transform: uppercase;
    white-space: nowrap;
    text-shadow: 1px 2px 3px rgba(0,0,0,.35);
  }

  /* 728x90 affiliate leaderboard */
  .leaderboard { left: 239px; top: 65px; width: 694px; height: 85px; }
  .leaderboard .flag { left: 0; top: 0; width: 150px; height: 85px; }
  .leaderboard .speakers { left: 113px; top: 8px; width: 107px; height: 73px;
    clip-path: polygon(0 0, 46% 0, 46% 100%, 54% 100%, 54% 0, 100% 0, 100% 100%, 0 100%); }
  .leaderboard .cta { left: 236px; top: 12px; font-size: 72px; line-height: .88; }
  .leaderboard .brand-box { position: absolute; left: 594px; top: 49px; width: 98px; height: 27px; background: var(--white); }
  .leaderboard .brand { left: 9px; top: 7px; font-size: 11px; }

  /* 160x600 affiliate skyscraper */
  .skyscraper { left: 37px; top: 136px; width: 153px; height: 571px; }
  .skyscraper .flag { left: 0; top: 200px; width: 153px; height: 331px; }
  .skyscraper .speakers { left: 5px; top: 361px; width: 145px; height: 176px;
    clip-path: polygon(51% 0, 100% 0, 100% 100%, 0 100%, 0 31%, 51% 31%); }
  .skyscraper .cta { left: 0; right: 0; top: 74px; text-align: center; font-size: 60px; }
  .skyscraper .footer { height: 41px; }
  .skyscraper .brand { left: 28px; top: 12px; font-size: 13px; }

  /* 600x500 email header */
  .email { left: 239px; top: 231px; width: 572px; height: 476px; }
  .email .flag { left: 0; top: 30px; width: 330px; height: 410px; }
  .email .speakers { left: 201px; top: 20px; width: 362px; height: 440px;
    clip-path: polygon(50.5% 0, 100% 0, 100% 100%, 0 100%, 0 31%, 50.5% 31%); }
  .email .cta { left: 53px; top: 42px; font-size: 70px; }
  .email .footer { height: 43px; }
  .email .brand { left: 20px; top: 11px; font-size: 16px; }

  /* 280x285 sidebar */
  .sidebar { left: 886px; top: 178px; width: 268px; height: 271px; }
  .sidebar .flag { left: 0; top: 0; width: 200px; height: 245px; }
  .sidebar .speakers { left: 112px; top: 52px; width: 154px; height: 195px;
    clip-path: polygon(54.5% 0, 100% 0, 100% 100%, 0 100%, 0 30%, 54.5% 30%); }
  .sidebar .cta { left: 66px; width: 132px; top: 6px; font-size: 54px; text-align: center; }
  .sidebar .footer { height: 38px; }
  .sidebar .brand { left: 14px; top: 9px; font-size: 15px; }

  /* 300x250 affiliate rectangle */
  .rectangle { left: 876px; top: 469px; width: 287px; height: 239px; }
  .rectangle .flag { left: 0; top: 0; width: 200px; height: 210px; }
  .rectangle .speakers { left: 134px; top: 39px; width: 152px; height: 180px;
    clip-path: polygon(54.6% 0, 100% 0, 100% 100%, 0 100%, 0 31%, 54.6% 31%); }
  .rectangle .cta { left: 100px; width: 117px; top: 2px; font-size: 48px; text-align: center; }
  .rectangle .footer { height: 34px; }
  .rectangle .brand { left: 14px; top: 8px; font-size: 15px; }

  /* 1180x300 website header */
  .header { left: 37px; top: 748px; width: 1126px; height: 287px; }
  .header .flag { left: 0; top: 0; width: 310px; height: 287px; }
  .header .speakers { left: 905px; top: 16px; width: 252px; height: 262px;
    clip-path: polygon(43% 0, 100% 0, 100% 100%, 0 100%, 0 31%, 43% 31%); }
  .header .cta { left: 169px; top: 46px; font-size: 158px; line-height: .88; }
  .header .footer { height: 43px; }
  .header .brand { left: 488px; top: 11px; font-size: 16px; }
</style>
</head>
<body>

  <div class="banner leaderboard">
    <svg class="flag" viewBox="0 0 100 100" preserveAspectRatio="none" role="img" aria-label="Waving American flag">
      <defs><linearGradient id="stripes-lb" x1="0" y1="0" x2="1" y2="1"><stop offset="0" stop-color="#f4f2f4"/><stop offset=".5" stop-color="#e8a7b2"/><stop offset="1" stop-color="#c8213a"/></linearGradient></defs>
      <path d="M0 0 H50 Q72 55 100 100 H0 Z" fill="url(#stripes-lb)"/>
      <path class="union" d="M0 0 H42 Q40 45 0 70 Z"/>
    </svg>
    <div class="speakers" role="img" aria-label="Pair of black bookshelf speakers"></div>
    <div class="cta">Shop Now</div>
    <div class="brand-box"><span class="brand">velmarsound</span></div>
  </div>

  <div class="banner skyscraper">
    <svg class="flag" viewBox="0 0 100 100" preserveAspectRatio="none" role="img" aria-label="Waving American flag">
      <defs><linearGradient id="stripes-sk" x1="0" y1="0" x2="1" y2="1"><stop offset="0" stop-color="#f4f2f4"/><stop offset=".5" stop-color="#e8a7b2"/><stop offset="1" stop-color="#c8213a"/></linearGradient></defs>
      <path d="M0 0 Q40 25 100 55 V100 H0 Z" fill="url(#stripes-sk)"/>
      <path class="union" d="M0 0 Q30 20 60 42 Q30 52 0 55 Z"/>
    </svg>
    <div class="speakers" role="img" aria-label="Home theater speaker system with towers, bookshelf speakers, subwoofer and center channel"></div>
    <div class="cta">Shop<br>Now</div>
    <div class="footer"><span class="brand">velmarsound</span></div>
  </div>

  <div class="banner email">
    <svg class="flag" viewBox="0 0 100 100" preserveAspectRatio="none" role="img" aria-label="Waving American flag">
      <defs><linearGradient id="stripes-em" x1="0" y1="0" x2="1" y2="1"><stop offset="0" stop-color="#f4f2f4"/><stop offset=".5" stop-color="#e8a7b2"/><stop offset="1" stop-color="#c8213a"/></linearGradient></defs>
      <path d="M0 0 Q20 40 100 75 V100 H0 Z" fill="url(#stripes-em)"/>
      <path class="union" d="M0 0 Q15 35 55 58 Q25 68 0 72 Z"/>
    </svg>
    <div class="speakers" role="img" aria-label="Home theater speaker system with towers, bookshelf speakers, subwoofer and center channel"></div>
    <div class="cta">Shop Now</div>
    <div class="footer"><span class="brand">velmarsound</span></div>
  </div>

  <div class="banner sidebar">
    <svg class="flag" viewBox="0 0 100 100" preserveAspectRatio="none" role="img" aria-label="Waving American flag">
      <defs><linearGradient id="stripes-sb" x1="0" y1="0" x2="1" y2="1"><stop offset="0" stop-color="#f4f2f4"/><stop offset=".5" stop-color="#e8a7b2"/><stop offset="1" stop-color="#c8213a"/></linearGradient></defs>
      <path d="M0 0 Q35 55 100 80 V100 H0 Z" fill="url(#stripes-sb)"/>
      <path class="union" d="M0 0 Q20 40 55 62 Q25 72 0 75 Z"/>
    </svg>
    <div class="speakers" role="img" aria-label="Home theater speaker system with towers, bookshelf speakers, subwoofer and center channel"></div>
    <div class="cta">Shop<br>Now</div>
    <div class="footer"><span class="brand">velmarsound</span></div>
  </div>

  <div class="banner rectangle">
    <svg class="flag" viewBox="0 0 100 100" preserveAspectRatio="none" role="img" aria-label="Waving American flag">
      <defs><linearGradient id="stripes-rc" x1="0" y1="0" x2="1" y2="1"><stop offset="0" stop-color="#f4f2f4"/><stop offset=".5" stop-color="#e8a7b2"/><stop offset="1" stop-color="#c8213a"/></linearGradient></defs>
      <path d="M0 0 Q35 50 100 80 V100 H0 Z" fill="url(#stripes-rc)"/>
      <path class="union" d="M0 0 Q20 38 55 60 Q25 70 0 73 Z"/>
    </svg>
    <div class="speakers" role="img" aria-label="Home theater speaker system with towers, bookshelf speakers, subwoofer and center channel"></div>
    <div class="cta">Shop<br>Now</div>
    <div class="footer"><span class="brand">velmarsound</span></div>
  </div>

  <div class="banner header">
    <svg class="flag" viewBox="0 0 100 100" preserveAspectRatio="none" role="img" aria-label="Waving American flag">
      <defs><linearGradient id="stripes-hd" x1="0" y1="0" x2="1" y2="1"><stop offset="0" stop-color="#f4f2f4"/><stop offset=".5" stop-color="#e8a7b2"/><stop offset="1" stop-color="#c8213a"/></linearGradient></defs>
      <path d="M0 10 Q25 70 100 100 H0 Z" fill="url(#stripes-hd)"/>
      <path class="union" d="M0 10 Q12 45 45 62 Q20 72 0 75 Z"/>
    </svg>
    <div class="footer"><span class="brand">velmarsound</span></div>
    <div class="speakers" role="img" aria-label="Home theater speaker system with towers, bookshelf speakers, subwoofer and center channel"></div>
    <div class="cta">Shop Now</div>
  </div>

</body>
</html>
```